Basic Web Design and coding (wordpress ideally). Needed live by 10th Feb!

Hi,

We are a Financial Wellness company that provides free seminars to help educate the general public and guide them to becoming debt free and prosperous.

Our company provides insurance, mortgage/ home loan and investment advice.

We require a fairly basic website that shouldn't require more then just a few pages.

The key elements to the site are as follows;

1: clean and easy to use (both on the front and back end). Clean calls to action and easy to use.

2: 4 "buttons" on the home page for the customer to choose which service they require from us which leads to a data capture form.

3: A (live?) calendar that shows all the seminars we provide across the country (location, date, time, etc) and also allows customers to register their attendance via the website. No payment is taken, just data capture. - this doesn't have to be live as long as it can be updated as needed.

4: Vorlix analytic

5: Responsive (phone, tablet etc)

Other than that its just Home, About Us, Services, Contact etc.

We already have the logo and color scheme (blue, green, white and black).

Here are a couple of templates that we like the design of - please note the position of the 4 "tabs/buttons" as these need to be seen on the home screen.

1) http://www.layoutquarry.com/demo/52036.html

2) http://www.layoutquarry.com/demo/45686.html

I will be choosing a design/contractor before the job closes.

Thank you.

Industry/Entity Type

Education

Number of Pages Required

5+ page

Requirements
Must have
• Coding. Brand continuity (color scheme), 4 buttons on the home screen, calendar.

```html
<!DOCTYPE html>
<html lang="en">
<head>
<meta charset="utf-8">
<title>Brightpath Wellness</title>
<link rel="stylesheet" href="https://fonts.googleapis.com/css2?family=Roboto:ital,wght@0,300;0,400;0,500;0,700;1,400&display=swap">
<style>
:root{
  --blue:#2b52a0;
  --blue-deep:#24488f;
  --green:#25a67c;
  --red:#d8262b;
  --ink:#333;
  --muted:#666;
  --line:#d9d9d9;
  --footer:#1c1c1c;
  --footer-text:#a8a8a8;
  --white:#fff;
}
*{box-sizing:border-box;margin:0;padding:0}
html,body{width:1200px;height:2447px;overflow:hidden}
body{position:relative;background:var(--white);font-family:"Roboto",Arial,sans-serif;color:var(--ink)}
.abs{position:absolute}

/* header */
.site-header{position:absolute;left:0;top:0;width:1200px;height:180px}
.nav-link{position:absolute;top:88px;font-size:17px;font-weight:500;color:#8a8a8a;text-decoration:none;letter-spacing:.5px}
.nav-link.is-active{color:var(--blue)}
.nav-link.is-active::after{content:"";position:absolute;left:0;right:0;bottom:-7px;height:3px;background:var(--blue)}
.brand{position:absolute;left:0;width:1200px;top:70px;text-align:center;font-size:28px;font-weight:500;color:var(--blue);display:flex;justify-content:center;align-items:center;gap:10px}
.brand-mark{width:16px;height:16px;border-radius:50%;background:var(--green)}

/* hero */
.hero{position:absolute;left:0;top:180px;width:1200px;height:495px;background:linear-gradient(180deg,#2e89b8 0%,#6aa9c8 30%,#a9c3cf 52%,#6f6a45 66%,#8a6a2c 80%,#4d3a1a 100%);text-align:center;color:var(--white)}
.hero-title{position:absolute;top:122px;width:100%;font-size:66px;font-weight:700;letter-spacing:1px}
.hero-text{position:absolute;left:165px;width:870px;top:208px;font-size:27px;font-weight:300;line-height:34px}
.hero-btn{position:absolute;left:497px;top:350px;width:214px;height:41px;background:var(--blue);color:var(--white);font-size:21px;line-height:41px}
.hero-dots{position:absolute;left:524px;top:478px;display:flex;gap:12px}
.hero-dots span{width:40px;height:3px;background:rgba(255,255,255,.45)}
.hero-dots span.on{background:var(--white)}
.brand-stripe{position:absolute;left:0;top:675px;width:1200px;height:8px;background:linear-gradient(90deg,var(--green),var(--blue))}

/* section headings */
.section-title{position:absolute;left:0;width:1200px;text-align:center;font-size:27px;font-weight:500;color:var(--blue)}
.section-tag{position:absolute;left:0;width:1200px;text-align:center;font-size:10px;font-style:italic;font-weight:500;color:#777}
.section-rule{position:absolute;left:548px;width:104px;height:3px;background:var(--green)}

/* service cards */
.service-card{position:absolute;top:797px;width:257px;height:300px;border:1px solid #e4e4e4;text-align:center}
.service-photo{position:absolute;left:7px;top:7px;width:241px;height:144px}
.service-name{position:absolute;top:163px;width:100%;font-size:23px;font-weight:500;color:var(--blue)}
.service-text{position:absolute;left:26px;width:205px;top:194px;font-size:10.5px;line-height:13.5px;color:#555}
.service-btn{position:absolute;left:86px;top:259px;width:84px;height:28px;border:2px solid var(--blue);color:var(--blue);font-size:13px;font-weight:500;line-height:24px}
.service-btn.is-solid{background:var(--blue);color:var(--white)}

/* feature band */
.feature-band{position:absolute;left:0;top:1139px;width:1200px;height:380px;background:var(--blue);color:var(--white);text-align:center}
.feature-icon{position:absolute;top:72px;width:76px;height:76px}
.feature-text{position:absolute;left:230px;width:740px;top:176px;font-size:21px;font-weight:500;line-height:28px}
.feature-btn{position:absolute;left:498px;top:296px;width:204px;height:42px;border:2px solid var(--white);font-size:21px;line-height:38px}

/* schedule */
.calendar-card{position:absolute;left:112px;top:1668px;width:339px;height:443px;border:2px solid #ddd;background:var(--white)}
.calendar-photo{position:absolute;left:8px;top:8px;width:319px;height:200px}
.calendar-month{position:absolute;top:228px;width:100%;text-align:center;font-size:31px;color:var(--green);letter-spacing:1px}
.calendar-grid{position:absolute;left:39px;top:275px;width:262px;display:grid;grid-template-columns:repeat(7,1fr);text-align:center;font-size:23px;line-height:24.5px;color:#333}
.calendar-grid .dow{background:var(--green);color:var(--white);font-size:21px;line-height:23px;margin-bottom:2px}
.calendar-grid .hl{color:var(--blue)}
.calendar-grid .sun{color:var(--red)}
.slider-arrow{position:absolute;top:1758px;width:28px;height:44px}

.event{position:absolute;left:566px;width:538px}
.event-date{font-size:11px;font-weight:500;color:#555}
.event-title{margin-top:4px;font-size:17px;font-weight:500;color:var(--blue)}
.event-text{margin:6px 0 0 8px;font-size:11.5px;font-style:italic;line-height:16px;color:#555}
.event-rule{position:absolute;left:566px;width:538px;height:2px;background:#ddd}

/* footer */
.site-footer{position:absolute;left:0;top:2205px;width:1200px;height:242px;background:var(--footer);color:var(--footer-text)}
.newsletter-title{position:absolute;left:74px;top:48px;font-size:22px;color:var(--green)}
.newsletter-field{position:absolute;left:74px;top:84px;width:307px;height:30px;background:#f3f3ee;font-size:13px;font-style:italic;color:#999;padding:8px 10px}
.newsletter-btn{position:absolute;left:381px;top:84px;width:52px;height:30px;background:var(--green);color:var(--white);font-size:13px;font-weight:700;text-align:center;line-height:30px}
.newsletter-note{position:absolute;left:74px;top:122px;width:370px;font-size:11px;line-height:15px}
.footer-col{position:absolute;top:40px}
.footer-col h4{font-size:17px;font-weight:700;color:var(--green);margin-bottom:8px}
.footer-col li{list-style:none;font-size:13px;line-height:25.5px}
.social{position:absolute;width:36px;height:36px;border:2px solid var(--green);border-radius:50%}
.footer-rule{position:absolute;left:74px;top:196px;width:1052px;height:1px;background:#3a3a3a}
.copyright{position:absolute;left:74px;top:212px;font-size:13px;color:#ddd}
.legal-links{position:absolute;right:74px;top:212px;display:flex;gap:24px;font-size:13px;color:#ddd}
</style>
</head>
<body>

<header class="site-header">
  <a class="nav-link is-active" style="left:218px">HOME</a>
  <a class="nav-link" style="left:349px">ABOUT</a>
  <div class="brand"><span class="brand-mark"></span>Brightpath Wellness</div>
  <a class="nav-link" style="left:789px">SERVICES</a>
  <a class="nav-link" style="left:923px">CONTACT</a>
</header>

<section class="hero" role="img" aria-label="Wheat field under a wide blue sky at sunset">
  <h1 class="hero-title">BE THE BOSS</h1>
  <p class="hero-text">We are a Financial Wellness company that provides free seminars to help educate the general public and guide them to becoming debt free and prosperous.</p>
  <div class="hero-btn">Learn more</div>
  <div class="hero-dots"><span class="on"></span><span></span><span></span></div>
</section>
<div class="brand-stripe"></div>

<h2 class="section-title" style="top:712px">Our Services</h2>
<p class="section-tag" style="top:747px">"Lorem ipsum dolor sit amet, consectetur adipiscing elit".</p>
<div class="section-rule" style="top:768px"></div>

<article class="service-card" style="left:60px">
  <div class="service-photo" role="img" aria-label="Stacks of coins" style="background:linear-gradient(135deg,#dfe6ee,#a8a08a 55%,#c9d3de)"></div>
  <h3 class="service-name">Service 1</h3>
  <p class="service-text">Lorem ipsum dolor sit amet, consectetur adipiscing elit. Ut in eros placerat, pulvinar lacus ac, iaculis urna. Donec volutpat feugiat nibh eget malesuada.</p>
  <div class="service-btn is-solid">More info</div>
</article>
<article class="service-card" style="left:334px">
  <div class="service-photo" role="img" aria-label="Hand touching a digital finance chart" style="background:linear-gradient(135deg,#1f3f6a,#5d8fc0 55%,#9cbbd8)"></div>
  <h3 class="service-name">Service 2</h3>
  <p class="service-text">Lorem ipsum dolor sit amet, consectetur adipiscing elit. Ut in eros placerat, pulvinar lacus ac, iaculis urna. Donec volutpat feugiat nibh eget malesuada.</p>
  <div class="service-btn">More info</div>
</article>
<article class="service-card" style="left:608px">
  <div class="service-photo" role="img" aria-label="Couple meeting with an adviser" style="background:linear-gradient(135deg,#c9b59c,#7e8f9f 60%,#d9d4cc)"></div>
  <h3 class="service-name">Service 3</h3>
  <p class="service-text">Lorem ipsum dolor sit amet, consectetur adipiscing elit. Ut in eros placerat, pulvinar lacus ac, iaculis urna. Donec volutpat feugiat nibh eget malesuada.</p>
  <div class="service-btn">More info</div>
</article>
<article class="service-card" style="left:882px">
  <div class="service-photo" role="img" aria-label="House keys being handed over" style="background:linear-gradient(135deg,#b23a2e,#e3c2ae 50%,#3b3b44)"></div>
  <h3 class="service-name">Service 1</h3>
  <p class="service-text">Lorem ipsum dolor sit amet, consectetur adipiscing elit. Ut in eros placerat, pulvinar lacus ac, iaculis urna. Donec volutpat feugiat nibh eget malesuada.</p>
  <div class="service-btn">More info</div>
</article>

<section class="feature-band">
  <svg class="feature-icon" style="left:407px" viewBox="0 0 76 76" fill="none" stroke="#fff" stroke-width="3">
    <rect x="4" y="6" width="68" height="44"/><line x1="2" y1="6" x2="74" y2="6"/>
    <line x1="22" y1="40" x2="22" y2="30"/><line x1="32" y1="40" x2="32" y2="22"/><line x1="42" y1="40" x2="42" y2="28"/><line x1="52" y1="40" x2="52" y2="18"/>
    <line x1="38" y1="50" x2="38" y2="58"/><line x1="38" y1="58" x2="26" y2="72"/><line x1="38" y1="58" x2="50" y2="72"/>
  </svg>
  <svg class="feature-icon" style="left:566px" viewBox="0 0 76 76" fill="none" stroke="#fff" stroke-width="3">
    <path d="M34 8 A30 30 0 1 0 68 42 L34 42 Z"/><path d="M42 4 A30 30 0 0 1 72 34 L42 34 Z"/>
  </svg>
  <svg class="feature-icon" style="left:725px" viewBox="0 0 76 76" fill="none" stroke="#fff" stroke-width="3">
    <path d="M58 12 A28 28 0 1 0 58 64"/><line x1="10" y1="32" x2="46" y2="32"/><line x1="10" y1="44" x2="44" y2="44"/>
  </svg>
  <p class="feature-text">Ut vitae lectus in metus congue posuere eu at lacus. Aliquam sollicitudin arcu eu ligula rhoncus, vel euismod orci cursus. Quisque eu risus at purus varius congue at nec enim.</p>
  <div class="feature-btn">Learn more</div>
</section>

<h2 class="section-title" style="top:1563px">Our Schedule</h2>
<p class="section-tag" style="top:1598px">"Lorem ipsum dolor sit amet, consectetur adipiscing elit".</p>
<div class="section-rule" style="top:1619px"></div>

<svg class="slider-arrow" style="left:76px" viewBox="0 0 28 44"><polyline points="24,4 6,22 24,40" fill="none" stroke="#c8c8c8" stroke-width="6"/></svg>
<svg class="slider-arrow" style="left:463px" viewBox="0 0 28 44"><polyline points="4,4 22,22 4,40" fill="none" stroke="#c8c8c8" stroke-width="6"/></svg>

<div class="calendar-card">
  <div class="calendar-photo" role="img" aria-label="Person leaping on a beach holding colourful balloons" style="background:linear-gradient(180deg,#7fc4c0 0%,#a9d2c4 55%,#e0c48f 80%,#c9a772 100%)"></div>
  <div class="calendar-month">· FEBRUARY ·</div>
  <div class="calendar-grid">
    <span class="dow">S</span><span class="dow">M</span><span class="dow">T</span><span class="dow">W</span><span class="dow">T</span><span class="dow">F</span><span class="dow">S</span>
    <span></span><span>1</span><span>2</span><span>3</span><span>4</span><span class="hl">5</span><span class="hl">6</span>
    <span class="sun">7</span><span>8</span><span class="hl">9</span><span>10</span><span>11</span><span>12</span><span>13</span>
    <span class="sun">14</span><span>15</span><span>16</span><span>17</span><span>18</span><span class="hl">19</span><span class="hl">20</span>
    <span class="hl">21</span><span>22</span><span>23</span><span>24</span><span>25</span><span>26</span><span>27</span>
    <span class="sun">28</span><span>29</span>
  </div>
</div>

<article class="event" style="top:1694px">
  <p class="event-date">February 9, 2016</p>
  <h3 class="event-title">Lorem Ipsum dolor amet.</h3>
  <p class="event-text">Lorem ipsum dolor sit amet, consectetur adipiscing elit. Duis in venenatis arcu. Donec et sapien nisl. Donec posuere dolor ut ipsum tempor fermentum. Integer posuere lacinia blandit. Praesent ac molestie elit, et accumsan sapien. Mauris tincidunt, erat vel molestie commodo,</p>
</article>
<div class="event-rule" style="top:1811px"></div>
<article class="event" style="top:1828px">
  <p class="event-date">February 9, 2016</p>
  <h3 class="event-title">Lorem Ipsum dolor amet.</h3>
  <p class="event-text">Lorem ipsum dolor sit amet, consectetur adipiscing elit. Duis in venenatis arcu. Donec et sapien nisl. Donec posuere dolor ut ipsum tempor fermentum. Integer posuere lacinia blandit. Praesent ac molestie elit, et accumsan sapien. Mauris tincidunt, erat vel molestie commodo,</p>
</article>
<div class="event-rule" style="top:1945px"></div>
<article class="event" style="top:1962px">
  <p class="event-date">February 9, 2016</p>
  <h3 class="event-title">Lorem Ipsum dolor amet.</h3>
  <p class="event-text">Lorem ipsum dolor sit amet, consectetur adipiscing elit. Duis in venenatis arcu. Donec et sapien nisl. Donec posuere dolor ut ipsum tempor fermentum. Integer posuere lacinia blandit. Praesent ac molestie elit, et accumsan sapien. Mauris tincidunt, erat vel molestie commodo,</p>
</article>
<div class="event-rule" style="top:2079px"></div>

<footer class="site-footer">
  <h3 class="newsletter-title">Get our newsletter</h3>
  <div class="newsletter-field">your email...</div>
  <div class="newsletter-btn">Submit</div>
  <p class="newsletter-note">Duis eu quam dui. Cras euismod ipsum et ligula aliquet blandit. Aliquam eu auctor tortor.</p>

  <div class="footer-col" style="left:529px"><h4>Menu</h4><ul><li>Home</li><li>About</li><li>Service</li><li>Contact</li></ul></div>
  <div class="footer-col" style="left:646px"><h4>Services</h4><ul><li>Service 1</li><li>Service 2</li><li>Service 3</li><li>Service 4</li></ul></div>
  <div class="footer-col" style="left:758px"><h4>Contact</h4><ul><li>+123.456.78901</li><li>email@domain.com</li><li>lorem ipsum street 123</li><li>12345</li></ul></div>

  <span class="social" style="left:975px;top:44px"></span>
  <span class="social" style="left:1032px;top:44px"></span>
  <span class="social" style="left:1090px;top:44px"></span>
  <span class="social" style="left:975px;top:88px"></span>
  <span class="social" style="left:1032px;top:88px"></span>
  <span class="social" style="left:1090px;top:88px"></span>

  <div class="footer-rule"></div>
  <p class="copyright">Copyright © 2015 All rights reserved.</p>
  <nav class="legal-links"><span>Terms &amp; Conditions</span><span>Privacy Policy</span><span>Refund Policy</span><span>Footer Menu</span></nav>
</footer>

</body>
</html>
```